2 x Wavelink Ads for "Bad Credit Car Loans" & "Single Parent Pensioner Car Loans"

We require a new "Bad Credit Car Loan" and "Single Parent Pensioner Car Loans - Advertisements for our Wavelink ads.
We are required to use the 20% text rule so all advertisements submitted MUST be tested by YOU the designer for the ability to use for the 20% text rule within the advertisement. Our previous Ads which have run for 8 Months have worked, however we require fresh new ads for our Marketing on Wavelink.
Target Market(s)
Bad Credit Car Finance & Pensioner Car Finance
Industry/Entity Type
Loan
Number of Pages Required
1 page
Font styles to use
Sans Serif
Requirements
Must have
- We require 2 x Wavelink Advertisments as Described - Existing ads have been uploaded.
Nice to have
- Must stand Out and Show what we are marketing
Should not have
- Not look cheap and tacky

```html
<!DOCTYPE html>
<html lang="en">
<head>
<meta charset="utf-8">
<title>Wavelink Ads – Bad Credit &amp; Pensioner Car Loans</title>
<link href="https://fonts.googleapis.com/css2?family=Roboto:wght@400;500;700;900&display=swap" rel="stylesheet">
<style>
  :root{
    --canvas:#eceef2;
    --panel:#ffffff;
    --panel-line:#dddfe2;
    --soft:#f6f7f9;
    --ink:#1d2129;
    --muted:#90949c;
    --label:#4b4f56;
    --brand:#4267b2;
    --ad-red:#d9342b;
    --ad-cream:#f7e9d9;
    --device:#222428;
    --tick:#4267b2;
  }
  *{box-sizing:border-box;margin:0;padding:0}
  html,body{width:1200px;height:2292px;overflow:hidden}
  body{background:var(--canvas);font-family:"Roboto",Arial,sans-serif;color:var(--ink);position:relative}

  .headline{position:absolute;top:34px;left:0;width:1200px;text-align:center}
  .headline h1{font-size:30px;font-weight:900;line-height:38px;color:var(--ink)}
  .headline p{font-size:24px;font-weight:700;line-height:32px;color:var(--ink)}

  .panel{position:absolute;left:120px;width:960px;background:var(--panel);border:1px solid var(--panel-line);border-radius:4px;overflow:hidden}
  .panel--feed{top:124px;height:680px}
  .panel--mobile{top:846px;height:700px}
  .panel--column{top:1590px;height:640px}

  .form{position:absolute;left:22px;top:22px;width:290px}
  .form-title{font-size:15px;font-weight:700;margin-bottom:4px}
  .form-sub{font-size:11px;color:var(--muted);margin-bottom:14px}
  .field{margin-bottom:14px}
  .field-label{font-size:11.5px;font-weight:500;color:var(--label);margin-bottom:5px}
  .field-note{font-size:10.5px;color:var(--muted);margin-bottom:5px;line-height:14px}
  .input{border:1px solid var(--panel-line);border-radius:3px;height:30px;padding:0 9px;font-size:12px;line-height:28px;color:var(--ink);background:#fff;white-space:nowrap;overflow:hidden}
  .input--area{height:58px;line-height:16px;padding-top:6px;white-space:normal}
  .input--select{width:150px;position:relative}
  .input--select::after{content:"";position:absolute;right:9px;top:12px;border:5px solid transparent;border-top-color:var(--label)}
  .link{font-size:11px;color:var(--brand);margin-bottom:14px}
  .page-pick{display:flex;align-items:center;gap:7px}
  .page-dot{width:14px;height:14px;background:var(--ad-red);border-radius:2px}

  .preview{position:absolute;left:330px;top:0;right:0;bottom:0;border-left:1px solid var(--panel-line);background:var(--soft)}
  .preview-title{font-size:13px;font-weight:700;padding:14px 18px 10px}
  .placement{display:flex;align-items:center;gap:10px;height:40px;padding:0 18px;border-top:1px solid var(--panel-line);background:#fff;font-size:12.5px;font-weight:500}
  .placement svg{flex:none}

  .post{position:absolute;left:40px;right:40px;top:96px;background:#fff;border:1px solid var(--panel-line);border-radius:3px}
  .post-head{display:flex;align-items:center;gap:9px;padding:10px 12px 6px}
  .post-avatar{width:32px;height:32px;background:var(--ad-red);border-radius:2px;flex:none}
  .post-name{font-size:12.5px;font-weight:700;color:var(--brand)}
  .post-meta{font-size:10px;color:var(--muted)}
  .post-like{margin-left:auto;border:1px solid var(--panel-line);border-radius:2px;font-size:10.5px;padding:3px 8px;color:var(--label)}
  .post-text{font-size:11.5px;padding:2px 12px 8px;color:var(--ink)}

  .banner{position:relative;background:var(--ad-red);overflow:hidden}
  .banner-title{position:absolute;color:#fff;font-weight:900;text-transform:uppercase;white-space:nowrap}
  .banner-title small{display:block;font-weight:500;letter-spacing:1px}
  .banner-art{position:absolute;background:linear-gradient(180deg,var(--ad-cream),#efd6bd);border-radius:40% 45% 12% 12%}
  .banner--feed{height:200px}
  .banner--feed .banner-title{left:34px;top:72px;font-size:25px;line-height:28px}
  .banner--feed .banner-title small{font-size:13px;line-height:18px}
  .banner--feed .banner-art{right:44px;top:78px;width:120px;height:60px}

  .post-foot{display:flex;align-items:center;gap:10px;padding:10px 12px;background:var(--soft);border-bottom:1px solid var(--panel-line)}
  .post-foot .copy{flex:1;min-width:0}
  .ad-head{font-size:14px;font-weight:700}
  .ad-desc{font-size:10.5px;color:var(--label);line-height:14px}
  .btn{border:1px solid #ccd0d5;background:#f6f7f9;border-radius:2px;font-size:11px;font-weight:700;padding:5px 10px;color:var(--label);white-space:nowrap}
  .post-actions{display:flex;gap:32px;padding:8px 14px;font-size:11px;font-weight:700;color:var(--muted)}
  .feed-bottom{position:absolute;left:0;right:0;bottom:0}

  .stage{position:absolute;left:0;right:0;bottom:0;background:var(--soft);border-top:1px solid var(--panel-line)}
  .panel--mobile .stage{top:160px}
  .panel--column .stage{top:200px}

  .device{position:absolute;left:50%;top:26px;width:196px;height:380px;margin-left:-98px;background:var(--device);border-radius:26px;padding:40px 10px}
  .device-screen{background:#fff;height:100%;overflow:hidden}
  .device-screen .post-head{padding:7px 7px 4px;gap:6px}
  .device-screen .post-avatar{width:20px;height:20px}
  .device-screen .post-name{font-size:9px}
  .device-screen .post-meta{font-size:7px}
  .device-screen .post-text{font-size:8px;line-height:10px;padding:0 7px 5px}
  .banner--mobile{height:96px}
  .banner--mobile .banner-title{left:9px;top:36px;font-size:8px;line-height:10px}
  .banner--mobile .banner-title small{font-size:5px;line-height:7px;letter-spacing:.6px}
  .banner--mobile .banner-art{right:8px;top:38px;width:38px;height:20px}
  .device-screen .post-foot{padding:6px 7px;gap:5px}
  .device-screen .ad-head{font-size:9px}
  .device-screen .ad-desc{font-size:7px;line-height:9px}
  .device-screen .btn{font-size:7px;padding:3px 5px}
  .stage-note{position:absolute;left:0;right:0;bottom:26px;text-align:center;font-size:10.5px;color:var(--muted);line-height:15px}

  .column-ad{position:absolute;left:60px;top:40px;width:280px}
  .banner--column{height:150px}
  .banner--column .banner-title{left:18px;top:56px;font-size:14px;line-height:16px}
  .banner--column .banner-title small{font-size:8px;line-height:11px}
  .banner--column .banner-art{right:18px;top:56px;width:72px;height:36px}
  .column-ad .ad-head{font-size:13px;margin-top:8px}
  .column-ad .ad-link{font-size:10.5px;color:var(--muted)}
  .column-ad .ad-desc{margin-top:3px}
</style>
</head>
<body>

<header class="headline">
  <h1>Highly noticeable ADS on all platforms and devices</h1>
  <p>Draws maximum attention with simple flat colors</p>
</header>

<!-- Desktop feed placement -->
<section class="panel panel--feed">
  <div class="form">
    <div class="form-title">Page &amp; Links</div>
    <div class="form-sub">Change your ad’s page and link options</div>
    <div class="field">
      <div class="field-label">Connect Wavelink Page</div>
      <div class="field-note">Your business is represented in ads by its Wavelink Page.</div>
      <div class="input input--select page-pick"><span class="page-dot"></span>DriveLend</div>
    </div>
    <div class="link">+ Turn Off News Feed Ads</div>
    <div class="field">
      <div class="field-label">Website URL</div>
      <div class="input">www.drivelend.com</div>
    </div>
    <div class="field">
      <div class="field-label">Headline</div>
      <div class="input">Bad Credit Car Finance</div>
    </div>
    <div class="field">
      <div class="field-label">Text</div>
      <div class="input input--area">Get the financing you need to buy a car, even with less than perfect credit</div>
    </div>
    <div class="field">
      <div class="field-label">Call to Action</div>
      <div class="input input--select">Learn More</div>
    </div>
    <div class="link">Hide Advanced Options</div>
    <div class="field">
      <div class="field-label">News Feed Link Description</div>
    </div>
  </div>

  <div class="preview">
    <div class="preview-title">Ad Preview</div>
    <div class="placement">
      <svg width="14" height="14" viewBox="0 0 14 14"><path d="M2 7.5l3 3 7-7" fill="none" stroke="var(--tick)" stroke-width="2.2"/></svg>
      Desktop News Feed
    </div>

    <article class="post">
      <div class="post-head">
        <span class="post-avatar"></span>
        <div><div class="post-name">DriveLend</div><div class="post-meta">Sponsored</div></div>
        <span class="post-like">Like Page</span>
      </div>
      <div class="post-text">Get the financing you need to buy a car, even with less than perfect credit</div>
      <div class="banner banner--feed">
        <div class="banner-title"><small>Single Parent</small>Pensioner Car Loans</div>
        <div class="banner-art" role="img" aria-label="Flat illustration of a small car"></div>
      </div>
      <div class="post-foot">
        <div class="copy">
          <div class="ad-head">Bad Credit Car Finance</div>
          <div class="ad-desc">A leader in bad credit auto financing for more than 10 years, we would like to help you with your next car.</div>
        </div>
        <span class="btn">Learn More</span>
      </div>
      <div class="post-actions"><span>Like</span><span>Comment</span><span>Share</span></div>
    </article>

    <div class="feed-bottom">
      <div class="placement">
        <svg width="14" height="14" viewBox="0 0 14 14"><path d="M2 7.5l3 3 7-7" fill="none" stroke="var(--tick)" stroke-width="2.2"/></svg>
        Mobile News Feed
      </div>
    </div>
  </div>
</section>

<!-- Mobile placement -->
<section class="panel panel--mobile">
  <div class="form">
    <div class="field">
      <div class="input">Bad Credit Car Finance</div>
    </div>
    <div class="field">
      <div class="field-label">Text</div>
      <div class="input input--area">Get the financing you need to buy a car, even with less than perfect credit</div>
    </div>
    <div class="field">
      <div class="field-label">Call to Action (optional)</div>
      <div class="input input--select">Learn More</div>
    </div>
    <div class="link">Hide Advanced Options</div>
    <div class="field">
      <div class="field-label">News Feed Link Description</div>
      <div class="input input--area">A leader in bad credit auto financing for more than 10 years, we would like to help you with your next car.</div>
    </div>
    <div class="field">
      <div class="field-label">Display Link</div>
      <div class="input">drivelend.com</div>
    </div>
    <div class="field">
      <div class="field-label">URL Parameters (optional)</div>
      <div class="input">Ex: key1=value1&amp;key2=value2</div>
    </div>
    <div class="field">
      <div class="field-label">Pixel Tracking</div>
    </div>
  </div>

  <div class="preview">
    <div class="placement">
      <svg width="14" height="14" viewBox="0 0 14 14"><path d="M2 7.5l3 3 7-7" fill="none" stroke="var(--tick)" stroke-width="2.2"/></svg>
      Mobile News Feed
    </div>
    <div class="placement">
      <svg width="14" height="14" viewBox="0 0 14 14"><path d="M2 7.5l3 3 7-7" fill="none" stroke="var(--tick)" stroke-width="2.2"/></svg>
      Pictura
    </div>
    <div class="placement">
      <svg width="14" height="14" viewBox="0 0 14 14"><path d="M2 7.5l3 3 7-7" fill="none" stroke="var(--tick)" stroke-width="2.2"/></svg>
      Partner Network
    </div>

    <div class="stage">
      <div class="device">
        <div class="device-screen">
          <div class="post-head">
            <span class="post-avatar"></span>
            <div><div class="post-name">DriveLend</div><div class="post-meta">Sponsored</div></div>
          </div>
          <div class="post-text">Get the financing you need to buy a car, even with less than perfect credit</div>
          <div class="banner banner--mobile">
            <div class="banner-title"><small>Single Parent</small>Pensioner Car Loans</div>
            <div class="banner-art" role="img" aria-label="Flat illustration of a small car"></div>
          </div>
          <div class="post-foot">
            <div class="copy">
              <div class="ad-head">Bad Credit Car Finance</div>
              <div class="ad-desc">drivelend.com</div>
            </div>
            <span class="btn">Learn More</span>
          </div>
        </div>
      </div>
      <div class="stage-note">This is how your ad appears in the mobile feed.<br>Preview may vary slightly once the ad is live.</div>
    </div>
  </div>
</section>

<!-- Right column placement -->
<section class="panel panel--column">
  <div class="form">
    <div class="field">
      <div class="input">Bad Credit Car Finance</div>
    </div>
    <div class="field">
      <div class="field-label">Text</div>
      <div class="input input--area">Get the financing you need to buy a car, even with less than perfect credit</div>
    </div>
    <div class="field">
      <div class="field-label">Call to Action (optional)</div>
      <div class="input input--select">Learn More</div>
    </div>
    <div class="link">Hide Advanced Options</div>
    <div class="field">
      <div class="field-label">News Feed Link Description</div>
      <div class="input input--area">A leader in bad credit auto financing for more than 10 years, we would like to help you with your next car.</div>
    </div>
    <div class="field">
      <div class="field-label">Display Link</div>
      <div class="input">drivelend.com</div>
    </div>
    <div class="field">
      <div class="field-label">URL Parameters (optional)</div>
      <div class="input">Ex: key1=value1&amp;key2=value2</div>
    </div>
  </div>

  <div class="preview">
    <div class="placement">
      <svg width="14" height="14" viewBox="0 0 14 14"><path d="M2 7.5l3 3 7-7" fill="none" stroke="var(--tick)" stroke-width="2.2"/></svg>
      Mobile News Feed
    </div>
    <div class="placement">
      <svg width="14" height="14" viewBox="0 0 14 14"><path d="M2 7.5l3 3 7-7" fill="none" stroke="var(--tick)" stroke-width="2.2"/></svg>
      Pictura
    </div>
    <div class="placement">
      <svg width="14" height="14" viewBox="0 0 14 14"><path d="M2 7.5l3 3 7-7" fill="none" stroke="var(--tick)" stroke-width="2.2"/></svg>
      Partner Network
    </div>
    <div class="placement">
      <svg width="14" height="14" viewBox="0 0 14 14"><path d="M2 7.5l3 3 7-7" fill="none" stroke="var(--tick)" stroke-width="2.2"/></svg>
      Desktop Right Column
    </div>

    <div class="stage">
      <div class="column-ad">
        <div class="banner banner--column">
          <div class="banner-title"><small>Single Parent</small>Pensioner<br>Car Loans</div>
          <div class="banner-art" role="img" aria-label="Flat illustration of a small car"></div>
        </div>
        <div class="ad-head">Bad Credit Car Finance</div>
        <div class="ad-link">drivelend.com</div>
        <div class="ad-desc">Get the financing you need to buy a car, even with less than perfect credit.</div>
      </div>
    </div>
  </div>
</section>

</body>
</html>
```